Create a new business card

I’m looking to update my business card to make it match the rest of my brand. I will include my current website as well as what my vehicle designs look like, etc..
What my business currently services
Weekly maintenance pool openings / closings
Equipment repair, including pumps, heaters, salt systems, filters, etc.
We install automatic covers and maintain them as well as provide preventative maintenance

I would like to include my name.
Darren Holcott.
My title
Owner
My email
Darren@tidewellnx.com
4015867120
Www.tidewellnx.com

```html
<!DOCTYPE html>
<html lang="en">
<head>
<meta charset="utf-8">
<title>Tidewell Pool Service – Business Card</title>
<link href="https://fonts.googleapis.com/css2?family=Rajdhani:wght@500;600;700&display=swap" rel="stylesheet">
<style>
  :root {
    --backdrop: #141d3b;
    --card: #dde3ea;
    --card-shade: #c5ced9;
    --navy: #253a7c;
    --orange: #e8752a;
    --sky: #35b8e8;
    --ink: #253a7c;
  }
  * { margin: 0; padding: 0; box-sizing: border-box; }
  html, body {
    width: 1200px; height: 900px; overflow: hidden;
    background: var(--backdrop);
    font-family: "Rajdhani", sans-serif;
  }
  .sheet {
    position: relative; width: 1200px; height: 900px;
    display: flex; flex-direction: column; align-items: center; justify-content: center; gap: 44px;
  }
  .card {
    position: relative; width: 640px; height: 366px;
    background: var(--card); overflow: hidden;
    box-shadow: 0 10px 28px rgba(0,0,0,.45);
  }
  .card-waves { position: absolute; inset: 0; width: 100%; height: 100%; }
  .wave-navy { fill: var(--navy); }
  .wave-orange { fill: var(--orange); }
  .wave-sky { fill: var(--sky); }
  .rule { stroke: var(--navy); stroke-width: 1.5; }

  .contact {
    position: absolute; right: 78px; top: 86px;
    text-align: right; color: var(--ink);
  }
  .contact-title { font-size: 19px; font-weight: 600; letter-spacing: .5px; }
  .contact-name { font-size: 42px; font-weight: 700; line-height: 1.1; margin-bottom: 8px; }
  .contact-line { font-size: 21px; font-weight: 600; line-height: 1.5; text-transform: uppercase; }
  .contact-phone { margin-bottom: 10px; }

  .brand {
    position: absolute; display: flex; align-items: center; gap: 10px;
    color: var(--navy); font-weight: 700; text-transform: uppercase;
  }
  .brand-dot { border-radius: 50%; background: var(--sky); flex: none; }
  .brand-front { left: 34px; bottom: 58px; font-size: 24px; line-height: 1; }
  .brand-front .brand-dot { width: 22px; height: 22px; }

  .backdrop-splash {
    position: absolute; left: 170px; top: 40px; width: 360px; height: 300px;
    border-radius: 50%;
    background: radial-gradient(closest-side, var(--card-shade), rgba(197,206,217,0));
  }
  .brand-back {
    left: 0; right: 0; top: 150px; justify-content: center; font-size: 40px;
  }
  .brand-back .brand-dot { width: 32px; height: 32px; }
  .back-web {
    position: absolute; left: 0; right: 0; top: 208px; text-align: center;
    color: var(--navy); font-size: 20px; font-weight: 700; letter-spacing: 1px;
  }
</style>
</head>
<body>
<main class="sheet">

  <section class="card card-front">
    <svg class="card-waves" viewBox="0 0 640 366" aria-hidden="true">
      <path class="wave-navy" d="M0 0H640V18C560 20 500 90 380 105C250 120 120 55 0 70Z"/>
      <path class="wave-orange" d="M0 70C120 55 250 120 380 105C500 90 560 20 640 18V40C560 50 500 118 380 138C250 158 140 104 0 134Z"/>
      <path class="wave-sky" d="M400 366C500 342 580 320 640 300V318C590 336 520 356 470 366Z"/>
      <path class="wave-orange" d="M520 366C570 352 610 340 640 332V366Z"/>
      <line class="rule" x1="330" y1="326" x2="600" y2="326"/>
    </svg>
    <div class="contact">
      <p class="contact-title">OWNER</p>
      <p class="contact-name">DARREN HOLCOTT</p>
      <p class="contact-line contact-phone">4015867120</p>
      <p class="contact-line">Darren@tidewellnx.com</p>
      <p class="contact-line">Www.tidewellnx.com</p>
    </div>
    <div class="brand brand-front">
      <span class="brand-dot"></span>
      <span class="brand-name">Tidewell Pool Service</span>
    </div>
  </section>

  <section class="card card-back">
    <div class="backdrop-splash" role="img" aria-label="Soft grey paint splash texture behind the company name"></div>
    <svg class="card-waves" viewBox="0 0 640 366" aria-hidden="true">
      <path class="wave-navy" d="M0 0H640V8C520 10 440 40 300 48C190 54 90 30 0 42Z"/>
      <path class="wave-orange" d="M0 42C90 30 190 54 300 48C360 45 400 38 430 32C400 60 360 90 300 96C190 104 90 80 0 96Z"/>
      <path class="wave-sky" d="M420 366C510 336 580 318 640 304V322C590 338 520 356 480 366Z"/>
      <path class="wave-orange" d="M540 366C580 354 615 344 640 338V366Z"/>
    </svg>
    <div class="brand brand-back">
      <span class="brand-dot"></span>
      <span class="brand-name">Tidewell Pool Service</span>
    </div>
    <p class="back-web">WWW.TIDEWELLNX.COM</p>
  </section>

</main>
</body>
</html>
```